Corporate Dinner Invite at Verolla for PMV

PMV is hosting a corporate dinner at the BRQ Conference and we need an email attachment invite for the event. Please use some images from this site for inspiration: https://www.verollaexample.com/fernparlor/

Invite Title:
Join us for dinner!

Event Details:
Tuesday, October 24th 2023 at 6:30pm
Verolla Chicago, Fern Parlor
347 W Harlow Ave, Chicago, IL 60622

Target Market(s)

Corporate Audience

Font styles to use
Script

Colors
0054AA
0677BA
7BADD7
CADEEF
E8F1F8

Requirements
Must have
• PMV logo, event date / time, event location details, photo(s) from Fern Parlor

```html
<!DOCTYPE html>
<html lang="en">
<head>
<meta charset="utf-8">
<title>Join us for dinner – PMV at Verolla</title>
<link href="https://fonts.googleapis.com/css2?family=Great+Vibes&family=Alegreya:wght@600;700&display=swap" rel="stylesheet">
<style>
  :root {
    --page-bg: #e6e7e9;
    --card-bg: #ffffff;
    --navy: #0d3a8e;
    --gold: #c9a77c;
    --frame-line: rgba(255,255,255,0.9);
    --bar-dark: #1e130c;
    --bar-mid: #4a2c16;
    --bar-glow: #b9742e;
    --counter: #e9e6e2;
  }
  * { margin: 0; padding: 0; box-sizing: border-box; }
  html, body {
    width: 1200px; height: 1200px; overflow: hidden;
    background: var(--page-bg);
  }
  .invite {
    position: absolute; left: 205px; top: 50px;
    width: 789px; height: 1104px;
    background: var(--card-bg);
    text-align: center;
    color: var(--navy);
    font-family: "Alegreya", Georgia, serif;
  }
  .invite__photo {
    position: absolute; left: 0; top: 0; width: 789px; height: 512px;
    background:
      radial-gradient(ellipse 60% 30% at 50% 58%, rgba(230,150,60,0.45), transparent 70%),
      radial-gradient(ellipse 40% 25% at 20% 35%, rgba(200,110,40,0.35), transparent 70%),
      linear-gradient(180deg, var(--bar-dark) 0%, var(--bar-mid) 45%, var(--bar-glow) 70%, #d9a35a 80%, var(--counter) 88%, #f4f2ef 100%);
  }
  .invite__frame {
    position: absolute; left: 20px; top: 22px; right: 19px; height: 490px;
    border: 1.5px solid var(--frame-line); border-bottom: none;
  }
  .invite__title {
    position: absolute; left: 0; right: 0; top: 568px;
    font-family: "Great Vibes", cursive;
    font-weight: 400; font-size: 96px; line-height: 1;
  }
  .invite__date {
    position: absolute; left: 0; right: 0; top: 715px;
    font-size: 31px; font-weight: 700; line-height: 1;
  }
  .venue-mark {
    position: absolute; left: 0; right: 0; top: 728px;
  }
  .venue-mark__circle {
    display: block; margin: 50px auto 0;
    width: 60px; height: 60px; border-radius: 50%;
    border: 1.5px solid var(--gold);
  }
  .venue-mark__name {
    display: block; margin-top: 10px;
    font-size: 27px; font-weight: 600; letter-spacing: 3px;
    color: var(--gold); line-height: 1;
  }
  .invite__venue {
    position: absolute; left: 0; right: 0; top: 895px;
    font-size: 26px; font-weight: 700; line-height: 40px;
  }
  .host-mark {
    position: absolute; left: 0; right: 0; top: 1040px;
    display: flex; justify-content: center; align-items: center; gap: 14px;
  }
  .host-mark__square {
    width: 40px; height: 40px; background: var(--navy);
  }
  .host-mark__name {
    font-size: 48px; font-weight: 700; line-height: 1; color: var(--navy);
  }
</style>
</head>
<body>
  <main class="invite">
    <div class="invite__photo" role="img" aria-label="Photo of cocktails lined up on a marble bar counter in the Fern Parlor lounge, warm blurred bar lights behind"></div>
    <div class="invite__frame"></div>

    <h1 class="invite__title">Join us for dinner!</h1>
    <p class="invite__date">Tuesday, October 24th 2023 at 6:30pm</p>

    <div class="venue-mark">
      <span class="venue-mark__circle"></span>
      <span class="venue-mark__name">VEROLLA</span>
    </div>

    <p class="invite__venue">
      Verolla Chicago, Fern Parlor<br>
      347 W Harlow Ave, Chicago, IL 60622
    </p>

    <div class="host-mark">
      <span class="host-mark__square"></span>
      <span class="host-mark__name">PMV</span>
    </div>
  </main>
</body>
</html>
```